Biz Card for Harrowfield Property Partners - HWPP

Harrowfield Property Partners is a commercial real estate acquisitions firm. We buy commercial property and need to raise capital from investors for each deal we buy. The vibe needs to be: give us your money, we will multiply it.
Our website: www.hrwpp-example.com
Competitors are: https://velmarholdings-example.com/, https://tribanquepartners-example.com/, http://www.ostrellecapital-example.com/
Target Market(s)
High Net Worth Individuals, Bankers, Insurance Companies, Commercial Real Estate Brokers.
Industry/Entity Type
Investment Banking
Contact Information for Business Card
Name, Title, Addess, Cell#, Office#, email, website
Requirements
Must have
- use one of our logos. See website for look and feel: www.hrwpp-example.com
Nice to have
- see website: www.hrwpp-example.com

```html
<!DOCTYPE html>
<html lang="en">
<head>
<meta charset="utf-8">
<title>Harrowfield Property Partners – Business Card</title>
<link href="https://fonts.googleapis.com/css2?family=Poppins:wght@400;500;600&display=swap" rel="stylesheet">
<style>
  :root {
    --backdrop: #d7d7d7;
    --navy: #0b2640;
    --navy-text: #10263d;
    --paper: #ffffff;
    --rule-light: #e9eef3;
  }
  * { box-sizing: border-box; margin: 0; padding: 0; }
  html, body {
    width: 1200px; height: 800px; overflow: hidden;
    background: var(--backdrop);
    font-family: "Poppins", Arial, sans-serif;
  }
  .stage { position: relative; width: 1200px; height: 800px; }

  .card {
    position: absolute; top: 283px;
    width: 429px; height: 238px;
    overflow: hidden;
  }
  .card--front { left: 111px; background: var(--paper); color: var(--navy-text); }
  .card--back  { left: 638px; background: var(--navy); color: var(--paper); }

  .front__rule {
    position: absolute; left: 0; right: 0; top: 21px;
    height: 2px; background: var(--navy);
  }
  .holder { position: absolute; left: 32px; top: 33px; }
  .holder__name { font-size: 11.5px; font-weight: 600; letter-spacing: 0.1px; }
  .holder__title { font-size: 8px; font-weight: 400; margin-top: 1px; }

  .contacts { position: absolute; left: 32px; top: 128px; list-style: none; }
  .contacts li {
    display: flex; align-items: center; gap: 6px;
    font-size: 8.5px; line-height: 13px;
  }
  .contacts svg { width: 7px; height: 7px; flex: none; fill: var(--navy); }

  .address {
    position: absolute; left: 32px; top: 192px;
    display: flex; gap: 6px;
    font-size: 8.5px; line-height: 13px; font-style: normal;
  }
  .address svg { width: 7px; height: 9px; margin-top: 2px; fill: var(--navy); flex: none; }

  .brand {
    position: absolute;
    display: flex; flex-direction: column; align-items: center; text-align: center;
  }
  .brand__dot { width: 48px; height: 48px; border-radius: 50%; }
  .brand__name {
    margin-top: 6px;
    font-size: 11px; font-weight: 500; line-height: 14px;
    letter-spacing: 2px; text-transform: uppercase;
  }
  .card--front .brand { left: 268px; top: 130px; width: 144px; }
  .card--front .brand__dot { background: var(--navy); }
  .card--front .brand__name { color: var(--navy); }

  .card--back .brand { left: 14px; top: 116px; width: 148px; }
  .card--back .brand__dot { width: 42px; height: 42px; background: var(--paper); }
  .card--back .brand__name { color: var(--paper); font-size: 10px; line-height: 13px; }

  .back__rule {
    position: absolute; left: 0; right: 0; top: 201px;
    height: 2px; background: var(--rule-light);
  }
  .back__web {
    position: absolute; right: 28px; top: 207px;
    font-size: 8.5px; letter-spacing: 0.4px;
  }
</style>
</head>
<body>
<main class="stage">
  <section class="card card--front" aria-label="Business card front">
    <div class="front__rule"></div>
    <div class="holder">
      <p class="holder__name">Julian Ashworth</p>
      <p class="holder__title">CEO/Founder</p>
    </div>
    <ul class="contacts">
      <li><svg viewBox="0 0 8 8"><path d="M2 0h4a1 1 0 0 1 1 1v6a1 1 0 0 1-1 1H2a1 1 0 0 1-1-1V1a1 1 0 0 1 1-1zm0 1v5h4V1z"/></svg>800-555-0147</li>
      <li><svg viewBox="0 0 8 8"><path d="M1.6 0.4l1.3 1.6-.7 1a5 5 0 0 0 2.8 2.8l1-.7 1.6 1.3-.8 1.2C3.8 7.4.6 4.2.4 1.2z"/></svg>(786) 555-0192</li>
      <li><svg viewBox="0 0 8 8"><path d="M0 1.5h8v5H0zM.4 1.8 4 4.4l3.6-2.6"/></svg>info@hrwpp-example.com</li>
      <li><svg viewBox="0 0 8 8"><circle cx="4" cy="4" r="3.6"/></svg>www.hrwpp-example.com</li>
    </ul>
    <address class="address">
      <svg viewBox="0 0 8 10"><path d="M4 0a4 4 0 0 1 4 4c0 3-4 6-4 6S0 7 0 4a4 4 0 0 1 4-4zm0 2.4a1.6 1.6 0 1 0 0 3.2 1.6 1.6 0 0 0 0-3.2z"/></svg>
      <span>415 Marbella Way, Suite 900<br>Lindenport, FL 33000</span>
    </address>
    <div class="brand">
      <span class="brand__dot"></span>
      <p class="brand__name">Harrowfield<br>Property Partners</p>
    </div>
  </section>

  <section class="card card--back" aria-label="Business card back">
    <div class="brand">
      <span class="brand__dot"></span>
      <p class="brand__name">Harrowfield<br>Property Partners</p>
    </div>
    <div class="back__rule"></div>
    <p class="back__web">WWW.HRWPP-EXAMPLE.COM</p>
  </section>
</main>
</body>
</html>
```